Quimby's Yard & Garden Center Business Card Update

I need an updated Business card design for my Lawn and Garden Center. We do Landscaping installs, Lawn Mowing, Snow Removal and also have a Garden Center Retail Division. I uploaded a few of our previous business cards to give an idea of what we are starting with. The main goal of this update is to simplify and modernize the business card, not all of the services that are on the previous cards has to be on the new one but I would still like to highlight our main services. There is also a sample of our logo that Can be used in the design.

Industry/Entity Type

Landscaping

Contact Information for Business Card

Morris Quimby
Morris@Quimbysyardandgarden.example
Business (555) 201-7784
Cell (555) 318-6092

Colors

Designer to choose colors to be used in the design.

Requirements
Must have
• Services Provided :
• Landscaping
• Lawn Maintenance
• Snow Removal
• Garden Center

```html
<!DOCTYPE html>
<html lang="en">
<head>
<meta charset="UTF-8">
<title>Quimby's Yard &amp; Garden Center — Business Card</title>
<link rel="stylesheet" href="https://fonts.googleapis.com/css2?family=Roboto:wght@400;500;700&display=swap">
<style>
  :root {
    --bg: #d3d4cf;
    --card: #f3f3f1;
    --green: #2b5a2a;
    --ink: #3a3a3a;
    --muted: #6b6b6b;
  }
  * { margin: 0; padding: 0; box-sizing: border-box; }
  html, body { width: 1200px; height: 1059px; overflow: hidden; }
  body {
    background: var(--bg);
    font-family: "Roboto", Arial, sans-serif;
    display: flex;
    flex-direction: column;
    align-items: center;
    justify-content: center;
    gap: 60px;
  }
  .card {
    position: relative;
    width: 700px;
    height: 400px;
    background: var(--card);
    box-shadow: 0 10px 24px rgba(0,0,0,0.12);
  }
  .brand {
    display: flex;
    align-items: center;
    gap: 14px;
    color: var(--green);
    font-weight: 500;
  }
  .brand-dot { border-radius: 50%; background: var(--green); flex: none; }

  /* Front */
  .card-front .brand { position: absolute; top: 60px; right: 60px; font-size: 46px; }
  .card-front .brand-dot { width: 34px; height: 34px; }
  .accent-bar { position: absolute; left: 0; top: 178px; width: 14px; height: 46px; background: var(--green); }
  .person { position: absolute; left: 44px; top: 176px; }
  .person-name { color: var(--green); font-weight: 500; font-size: 30px; letter-spacing: 0.5px; }
  .person-title { color: var(--muted); font-size: 15px; margin-top: 2px; }
  .divider { position: absolute; left: 44px; right: 0; top: 242px; height: 1.5px; background: var(--green); }
  .contacts { position: absolute; left: 60px; top: 262px; list-style: none; }
  .contacts li { display: flex; align-items: center; gap: 10px; font-size: 17px; color: var(--muted); line-height: 28px; }
  .contacts svg { width: 14px; height: 14px; flex: none; fill: var(--green); }

  /* Back */
  .card-back { display: flex; flex-direction: column; align-items: center; }
  .card-back .brand { margin-top: 110px; font-size: 64px; }
  .card-back .brand-dot { width: 46px; height: 46px; }
  .services-heading { margin-top: 70px; color: var(--green); font-weight: 700; font-size: 22px; letter-spacing: 0.5px; }
  .services-list { margin-top: 10px; color: var(--ink); font-size: 18px; letter-spacing: 0.8px; }
</style>
</head>
<body>
  <section class="card card-front">
    <div class="brand"><span class="brand-dot"></span>Quimby's</div>
    <div class="accent-bar"></div>
    <div class="person">
      <div class="person-name">MORRIS QUIMBY</div>
      <div class="person-title">Director</div>
    </div>
    <div class="divider"></div>
    <ul class="contacts">
      <li><svg viewBox="0 0 24 24"><path d="M6.6 10.8a15 15 0 0 0 6.6 6.6l2.2-2.2a1 1 0 0 1 1-.25 11.4 11.4 0 0 0 3.6.57 1 1 0 0 1 1 1V20a1 1 0 0 1-1 1A17 17 0 0 1 3 4a1 1 0 0 1 1-1h3.5a1 1 0 0 1 1 1c0 1.25.2 2.45.57 3.57a1 1 0 0 1-.25 1z"/></svg>(555) 201-7784</li>
      <li><svg viewBox="0 0 24 24"><path d="M7 2h10a2 2 0 0 1 2 2v16a2 2 0 0 1-2 2H7a2 2 0 0 1-2-2V4a2 2 0 0 1 2-2zm0 3v13h10V5z"/></svg>(555) 318-6092</li>
      <li><svg viewBox="0 0 24 24"><path d="M3 5h18a1 1 0 0 1 1 1v12a1 1 0 0 1-1 1H3a1 1 0 0 1-1-1V6a1 1 0 0 1 1-1zm1 2.4V17h16V7.4l-8 5.3z"/></svg>Morris@Quimbysyardandgarden.example</li>
      <li><svg viewBox="0 0 24 24"><path d="M12 2a10 10 0 1 0 0 20 10 10 0 0 0 0-20zm6.9 9h-3a15 15 0 0 0-1.3-6A8 8 0 0 1 18.9 11zM12 4.1A13 13 0 0 1 13.9 11h-3.8A13 13 0 0 1 12 4.1zM9.4 5a15 15 0 0 0-1.3 6h-3A8 8 0 0 1 9.4 5zM5.1 13h3a15 15 0 0 0 1.3 6 8 8 0 0 1-4.3-6zm6.9 6.9a13 13 0 0 1-1.9-6.9h3.8a13 13 0 0 1-1.9 6.9zm2.6-.9a15 15 0 0 0 1.3-6h3a8 8 0 0 1-4.3 6z"/></svg>www.Quimbysyardandgarden.example</li>
    </ul>
  </section>

  <section class="card card-back">
    <div class="brand"><span class="brand-dot"></span>Quimby's</div>
    <h2 class="services-heading">SERVICES PROVIDED :</h2>
    <p class="services-list">Landscaping | Lawn Maintenance | Snow Removal | Garden Center</p>
  </section>
</body>
</html>
```